Business Card Project for Firm Deck Hoisting

Business name is "Firm Deck Hoisting" we are a scaffolding & rigging business specialising in local and remote work for:
- scaffolding (residential, commercial, industrial)
- rigging
-man material hoists
- swing stages
- labour hire

On the back of the card I would like FDH as the symbol / logo. I have attached the logos we have had created by sketch harbour. We would like to use bold colours – preferably as the same colour scheme as the logo.

Target Market(s)

Construction business

Industry/Entity Type

Construction

Contact Information for Business Card

name: Owen Pellew
Title: Director
Phone: 0491 572 864
Address: PO BOX 3251, Paralowie SA 5108
Email: owen@firmdeckhoisting.com.au
Website: www.firmdeckhoisting.com.au

Font styles to use
Sans Serif

Requirements
Must have
• Must use existing logo & prefering using bold colours
Nice to have
• Would be nice to have a line of dot points in what we specialise in but not essential
• Would be nice to see some designs with a slogan but not essential
Should not have
• NA

```html
<!DOCTYPE html>
<html lang="en">
<head>
<meta charset="utf-8">
<title>Firm Deck Hoisting – Business Cards</title>
<link href="https://fonts.googleapis.com/css2?family=Lato:wght@400;700&display=swap" rel="stylesheet">
<style>
  :root {
    --brand-blue: #2a74bd;
    --ink: #141414;
    --paper: #ffffff;
    --backdrop: #e9e9e7;
  }
  * { margin: 0; padding: 0; box-sizing: border-box; }
  html, body {
    width: 1200px; height: 901px; overflow: hidden;
    background: var(--backdrop);
    font-family: "Lato", Arial, sans-serif;
  }
  .sheet {
    position: relative; width: 1200px; height: 901px;
    display: flex; align-items: center; justify-content: center; gap: 40px;
  }
  .card {
    position: relative; width: 560px; height: 320px; overflow: hidden;
    box-shadow: 0 6px 18px rgba(0,0,0,0.18);
  }

  /* Front: blue */
  .card--front { background: var(--brand-blue); color: var(--paper); }
  .card--front .brand {
    position: absolute; left: 0; right: 0; top: 112px;
    display: flex; align-items: center; justify-content: center; gap: 14px;
  }
  .brand__square { width: 22px; height: 22px; background: var(--paper); }
  .brand__name { font-weight: 700; font-size: 34px; letter-spacing: 1px; text-transform: uppercase; }
  .services {
    position: absolute; left: 40px; right: 40px; top: 200px;
    text-align: center; font-size: 15px; line-height: 1.5;
  }

  /* Back: white */
  .card--back { background: var(--paper); color: var(--ink); }
  .card--back .brand {
    position: absolute; left: 40px; top: 40px;
    display: flex; align-items: center; gap: 12px;
  }
  .card--back .brand__square { background: var(--brand-blue); width: 18px; height: 18px; }
  .card--back .brand__name { font-size: 26px; color: var(--ink); }
  .contact {
    position: absolute; left: 40px; top: 96px;
    font-size: 14px; line-height: 1.45;
  }
  .contact__row { display: flex; align-items: center; gap: 8px; }
  .contact__row svg { width: 12px; height: 12px; fill: var(--brand-blue); }
  .person { position: absolute; right: 40px; top: 172px; }
  .person__name { color: var(--brand-blue); font-size: 24px; }
  .person__title { font-size: 14px; }
  .swoosh { position: absolute; left: 0; top: 0; width: 560px; height: 320px; }
  .website {
    position: absolute; left: 0; right: 0; bottom: 12px;
    text-align: center; color: var(--paper); font-size: 14px;
  }
</style>
</head>
<body>
<main class="sheet">
  <section class="card card--front">
    <div class="brand">
      <span class="brand__square"></span>
      <span class="brand__name">Firm Deck Hoisting</span>
    </div>
    <p class="services">scaffolding (residential, commercial, industrial)<br>
      • rigging • man material hoists • swing stages • labour hire</p>
  </section>

  <section class="card card--back">
    <svg class="swoosh" viewBox="0 0 560 320" aria-hidden="true">
      <path d="M0 196 C150 260 350 292 560 258 L560 320 L0 320 Z" fill="#141414"/>
      <path d="M0 210 C150 274 350 304 560 274 L560 320 L0 320 Z" fill="#ffffff"/>
      <path d="M0 218 C150 282 350 312 560 282 L560 320 L0 320 Z" fill="#2a74bd"/>
    </svg>
    <div class="brand">
      <span class="brand__square"></span>
      <span class="brand__name">Firm Deck Hoisting</span>
    </div>
    <div class="contact">
      <div class="contact__line">PO BOX 3251</div>
      <div class="contact__line">Harlow Creek SA 5120</div>
      <div class="contact__row">
        <svg viewBox="0 0 24 24"><path d="M6.6 10.8a15 15 0 0 0 6.6 6.6l2.2-2.2c.3-.3.7-.4 1-.2 1.1.4 2.3.6 3.6.6.6 0 1 .4 1 1V20c0 .6-.4 1-1 1A17 17 0 0 1 3 4c0-.6.4-1 1-1h3.5c.6 0 1 .4 1 1 0 1.3.2 2.5.6 3.6.1.3 0 .7-.2 1z"/></svg>
        <span>0491 572 864</span>
      </div>
      <div class="contact__row">
        <svg viewBox="0 0 24 24"><path d="M2 5h20v14H2z M2 5l10 8 10-8" stroke="#fff" stroke-width="1.5"/></svg>
        <span>owen@firmdeckhoisting.com.au</span>
      </div>
    </div>
    <div class="person">
      <div class="person__name">Owen Pellew</div>
      <div class="person__title">Director</div>
    </div>
    <div class="website">www.firmdeckhoisting.com.au</div>
  </section>
</main>
</body>
</html>
```